Enhance existing websites

Hello,

With my very limited web design knowledge I have designed my own websites...
Trailquote.example
Rovervalue.example

Whilst I have been very happy with the response I have received I feel the sites need enhancing. Here is what I would like to change..

1, Place a shadow around the whole pages outline so it has a 3d effect with a better background colour.

2, Improve the 'Request a valuation' tab so it stands out, maybe to also insert a curved arrow(s) to direct customer to click 'request a valuation' . Naturally this would need to be done on each page.

3, The testimonials of the 'what customers say' to change every few seconds.

4, The front page image to change every few seconds to a image of my choice.

5, any other suggestions you feel would benefit my site (obviously willing to pay extra for this and within this site)

6, given my limited knowledge my html code will surely need tidying also

7, if possible any changes not to affect my very good google ratings.

Price paid is for both sites as they're practically identical.

Thanks in advance

Glen

```html
<!DOCTYPE html>
<html lang="en">
<head>
<meta charset="utf-8">
<title>Trail Quote – The UK's largest buyer of touring caravans</title>
<link rel="stylesheet" href="https://fonts.googleapis.com/css2?family=Archivo+Black&family=Arimo:ital,wght@0,400;0,700;1,400&family=Open+Sans:wdth,wght@75,300&family=Oswald:wght@300;400;500&family=Walter+Turncoat&display=swap">
<style>
  :root {
    --brand-blue: #3b86c6;
    --brand-blue-dark: #2a6ca6;
    --sky-top: #2f7fc2;
    --sky-bottom: #6fb0e0;
    --accent-green: #7aab1f;
    --accent-green-dark: #5e8a12;
    --text-dark: #333333;
    --text-mid: #555555;
    --text-light: #777777;
    --rule: #d6d6d6;
    --panel-grey: #ebebeb;
    --band-grey: #e4e4e4;
    --white: #ffffff;
    --map-grey: #c4c4c4;
  }
  * { box-sizing: border-box; margin: 0; padding: 0; }
  html, body { width: 769px; height: 1200px; overflow: hidden; background: var(--white); }
  body { font-family: "Arimo", Arial, sans-serif; color: var(--text-dark); }

  .page {
    position: relative;
    width: 705px;
    height: 1100px;
    transform: scale(1.09078);
    transform-origin: 0 0;
    background: var(--white);
  }
  .abs { position: absolute; }

  .thin-heading {
    font-family: "Open Sans", sans-serif;
    font-weight: 300;
    font-stretch: 75%;
    color: var(--text-dark);
    white-space: nowrap;
  }

  /* Header */
  .brand-name { left: 38px; top: 8px; font-size: 31px; color: var(--brand-blue); letter-spacing: -0.5px; }
  .tagline { left: 38px; top: 42px; font-size: 10px; color: var(--text-dark); }
  .share { right: 36px; top: 13px; display: flex; align-items: center; gap: 5px; font-size: 12px; color: var(--text-dark); }
  .share-square { width: 15px; height: 15px; border-radius: 2px; background: #4ab3e8; }
  .share-square.alt { background: #3d5c99; }
  .contact { right: 36px; top: 41px; display: flex; align-items: center; gap: 6px; font-size: 9px; color: var(--text-mid); }
  .contact .phone { font-size: 11px; color: var(--text-dark); }
  .header-band { left: 0; top: 61px; width: 705px; height: 15px; background: linear-gradient(#f2f2f2, #dedede); }

  /* Navigation */
  .nav { left: 0; top: 76px; width: 705px; height: 40px; background: var(--white); border-bottom: 1px solid var(--rule); }
  .nav-list { position: absolute; left: 38px; top: 8px; display: flex; list-style: none; font-size: 12px; }
  .nav-item { display: block; height: 26px; line-height: 26px; margin-right: 30px; color: var(--text-dark); }
  .nav-item.current { background: var(--brand-blue); color: var(--white); padding: 0 13px; margin-right: 22px; position: relative; }
  .nav-item.current::after { content: ""; position: absolute; left: 50%; bottom: -4px; margin-left: -4px; border: 4px solid transparent; border-bottom: 0; border-top-color: var(--brand-blue); }

  .upper-panel { left: 0; top: 116px; width: 705px; height: 356px; background: var(--panel-grey); }

  /* Hero */
  .hero-frame { left: 38px; top: 130px; width: 630px; height: 250px; background: var(--white); box-shadow: 0 8px 10px -6px rgba(0,0,0,0.35); }
  .hero-image { left: 42px; top: 136px; width: 622px; height: 240px; background: linear-gradient(180deg, var(--sky-top) 0%, var(--sky-bottom) 70%, #d9cbb0 100%); }
  .hero-line1 { left: 72px; top: 157px; font-size: 27px; color: var(--white); }
  .hero-line2 { left: 72px; top: 192px; font-family: "Archivo Black", sans-serif; font-size: 29px; color: var(--white); letter-spacing: 1px; }
  .hero-line3 { left: 72px; top: 228px; font-family: "Archivo Black", sans-serif; font-size: 18px; color: var(--white); letter-spacing: 1.5px; }
  .hero-sub { left: 72px; top: 268px; font-family: "Oswald", sans-serif; font-weight: 300; font-size: 14px; color: var(--white); letter-spacing: 0.3px; }
  .valuation-btn { left: 70px; top: 297px; width: 254px; height: 30px; background: linear-gradient(#8cc027, var(--accent-green)); border-bottom: 3px solid var(--accent-green-dark); box-shadow: 2px 3px 4px rgba(0,0,0,0.3); display: flex; align-items: center; gap: 9px; padding-left: 7px; font-family: "Oswald", sans-serif; font-size: 16px; color: var(--white); white-space: nowrap; }
  .valuation-btn b { font-weight: 500; }

  /* Features */
  .features { left: 38px; top: 405px; width: 630px; height: 51px; display: flex; background: var(--white); border: 1px solid var(--rule); list-style: none; }
  .feature { flex: 1; display: flex; align-items: center; gap: 10px; padding-left: 9px; border-right: 1px solid var(--rule); font-size: 9.5px; line-height: 11.5px; color: var(--text-mid); }
  .feature:last-child { border-right: 0; }
  .feature svg { flex: 0 0 auto; }

  /* How it works */
  .how-panel { left: 0; top: 472px; width: 705px; height: 250px; background: var(--panel-grey); }
  .how-heading { left: 0; top: 481px; width: 705px; text-align: center; font-size: 31px; line-height: 40px; }
  .step { top: 535px; width: 200px; height: 122px; background: var(--white); border: 1px solid var(--rule); text-align: center; padding-top: 8px; }
  .step-icon { height: 26px; display: flex; align-items: center; justify-content: center; }
  .step-title { font-size: 21px; line-height: 26px; margin-top: 6px; }
  .step-text { font-size: 9.5px; line-height: 12px; color: var(--text-dark); padding: 6px 5px 0; }

  .selling-note { left: 59px; top: 690px; font-family: "Walter Turncoat", cursive; font-size: 12px; color: var(--text-dark); }
  .note-arrow { left: 205px; top: 703px; }
  .start-btn { left: 262px; top: 701px; width: 180px; height: 38px; background: linear-gradient(#4a95d3, var(--brand-blue-dark)); border-bottom: 3px solid #1f5585; box-shadow: 2px 3px 4px rgba(0,0,0,0.3); display: flex; align-items: center; gap: 8px; padding-left: 8px; font-family: "Oswald", sans-serif; font-size: 19px; color: var(--white); }

  /* Collection & testimonials */
  .uk-map { left: 38px; top: 765px; width: 122px; height: 166px; background: radial-gradient(ellipse at 55% 55%, var(--map-grey) 0%, #dcdcdc 60%, var(--white) 100%); }
  .section-title { font-size: 30px; line-height: 40px; }
  .collection-title { left: 176px; top: 760px; }
  .collection-sub { left: 177px; top: 810px; font-size: 13px; color: var(--text-dark); }
  .areas { top: 846px; list-style: none; font-size: 8.5px; line-height: 16.3px; color: var(--text-dark); }
  .areas li::before { content: "›"; margin-right: 4px; color: var(--text-mid); }
  .testimonials-title { left: 486px; top: 760px; }
  .quote { left: 488px; top: 812px; width: 179px; height: 75px; background: var(--accent-green); border-radius: 4px; padding: 11px 10px 0 14px; font-style: italic; font-size: 9.5px; line-height: 11.5px; color: var(--white); }
  .quote-tail { left: 628px; top: 886px; }
  .quote-name { right: 38px; top: 905px; font-style: italic; font-size: 10px; color: var(--text-dark); text-align: right; }
  .quote-model { right: 38px; top: 918px; font-style: italic; font-size: 8px; color: var(--text-light); text-align: right; }

  /* Partner tiles */
  .partner-band { left: 0; top: 945px; width: 705px; height: 102px; background: var(--band-grey); }
  .partner-grid { left: 38px; top: 963px; width: 632px; display: grid; grid-template-columns: repeat(15, 33px); column-gap: 6px; row-gap: 3px; }
  .partner { width: 33px; height: 33px; background: var(--white); border: 1px solid #cfcfcf; display: flex; align-items: center; justify-content: center; }
  .partner span { width: 23px; height: 13px; border-radius: 6px; background: #9aa7b4; }
  .partner:nth-child(3n) span { background: #c9463a; }
  .partner:nth-child(4n) span { background: #2f5f9e; width: 18px; height: 18px; border-radius: 50%; }
  .partner:nth-child(5n) span { background: #6b8e3a; }
  .partner:nth-child(7n) span { background: #d88a2a; border-radius: 2px; }

  /* Footer */
  .footer { left: 0; top: 1047px; width: 705px; height: 53px; background: var(--white); border-top: 1px solid var(--rule); }
  .footer-links { left: 41px; top: 1069px; display: flex; list-style: none; font-size: 8.5px; color: var(--text-dark); }
  .footer-links li + li::before { content: "|"; margin: 0 12px; }
  .footer-company { left: 530px; top: 1056px; font-size: 10.5px; color: var(--text-dark); }
  .footer-address { left: 530px; top: 1070px; font-size: 7.5px; color: var(--text-mid); }
  .footer-copy { left: 530px; top: 1082px; font-size: 6.5px; color: var(--text-mid); }
</style>
</head>
<body>
<div class="page">

  <header>
    <div class="abs brand-name">trailquote</div>
    <div class="abs tagline">The UK's largest buyer of touring caravans</div>
    <div class="abs share">Share us <span class="share-square"></span><span class="share-square alt"></span></div>
    <div class="abs contact">
      <svg width="11" height="8" viewBox="0 0 11 8"><rect x="0.5" y="0.5" width="10" height="7" fill="#bbb" stroke="#999"/><path d="M0.5 0.5 L5.5 4.5 L10.5 0.5" fill="none" stroke="#888"/></svg>
      <span>info@trailquote.example</span>
      <svg width="11" height="11" viewBox="0 0 11 11" style="margin-left:10px"><rect x="0" y="0" width="11" height="11" rx="2" fill="#bbb"/><path d="M3 2.5 C2 4 3.5 7.5 7.5 8.5 L8.5 7 L7 6 L6 6.8 C5 6.2 4.5 5.6 4 4.6 L4.8 3.8 L4 2 Z" fill="#fff"/></svg>
      <span class="phone">0800 000 4417</span>
    </div>
    <div class="abs header-band"></div>
  </header>

  <nav class="abs nav">
    <ul class="nav-list">
      <li><span class="nav-item current">Home</span></li>
      <li><span class="nav-item">How it Works</span></li>
      <li><span class="nav-item">FAQ's</span></li>
      <li><span class="nav-item">Contact us</span></li>
    </ul>
  </nav>

  <div class="abs upper-panel"></div>

  <section class="hero">
    <div class="abs hero-frame"></div>
    <div class="abs hero-image" role="img" aria-label="Photo of a white touring caravan on sand under a blue sky with clouds"></div>
    <div class="abs hero-line1">The UK's</div>
    <div class="abs hero-line2">LARGEST BUYER</div>
    <div class="abs hero-line3">OF TOURING CARAVANS</div>
    <div class="abs hero-sub">SELL YOUR CARAVAN QUICKLY AND SECURELY</div>
    <div class="abs valuation-btn">
      <svg width="15" height="15" viewBox="0 0 15 15"><circle cx="7.5" cy="7.5" r="7.5" fill="#fff"/><path d="M5.5 4 L11 7.5 L5.5 11 Z" fill="#7aab1f"/></svg>
      <span>Request a <b>FREE</b> Caravan Valuation</span>
    </div>
  </section>

  <ul class="abs features">
    <li class="feature"><svg width="26" height="24" viewBox="0 0 26 24"><rect x="1" y="4" width="19" height="19" rx="2" fill="none" stroke="#3b86c6" stroke-width="2"/><path d="M5 12 L10 17 L24 2" fill="none" stroke="#3b86c6" stroke-width="3.5"/></svg><span>Genuine online or verbal offer to purchase</span></li>
    <li class="feature"><svg width="26" height="24" viewBox="0 0 26 24"><rect x="1" y="4" width="19" height="19" rx="2" fill="none" stroke="#3b86c6" stroke-width="2"/><path d="M5 12 L10 17 L24 2" fill="none" stroke="#3b86c6" stroke-width="3.5"/></svg><span>Excellent prices offered and paid</span></li>
    <li class="feature"><svg width="26" height="24" viewBox="0 0 26 24"><rect x="1" y="4" width="19" height="19" rx="2" fill="none" stroke="#3b86c6" stroke-width="2"/><path d="M5 12 L10 17 L24 2" fill="none" stroke="#3b86c6" stroke-width="3.5"/></svg><span>No admin fees or hidden charges</span></li>
    <li class="feature"><svg width="26" height="24" viewBox="0 0 26 24"><rect x="1" y="4" width="19" height="19" rx="2" fill="none" stroke="#3b86c6" stroke-width="2"/><path d="M5 12 L10 17 L24 2" fill="none" stroke="#3b86c6" stroke-width="3.5"/></svg><span>Friendly professi-<br>onal, no hassle service</span></li>
    <li class="feature"><svg width="26" height="24" viewBox="0 0 26 24"><rect x="1" y="4" width="19" height="19" rx="2" fill="none" stroke="#3b86c6" stroke-width="2"/><path d="M5 12 L10 17 L24 2" fill="none" stroke="#3b86c6" stroke-width="3.5"/></svg><span>Instant cash or faster payment bank transfer</span></li>
  </ul>

  <section class="how">
    <div class="abs how-panel"></div>
    <h2 class="abs thin-heading how-heading">Here's How It Works!</h2>

    <article class="abs step" style="left:38px">
      <div class="step-icon"><svg width="22" height="26" viewBox="0 0 22 26"><path d="M1 1 H15 L21 7 V25 H1 Z" fill="none" stroke="#3b86c6" stroke-width="2"/><path d="M15 1 V7 H21" fill="none" stroke="#3b86c6" stroke-width="2"/><path d="M5 12 H17 M5 16 H17 M5 20 H17" stroke="#3b86c6" stroke-width="1.8"/></svg></div>
      <h3 class="thin-heading step-title">Enter your details</h3>
      <p class="step-text">Simply call us on our freephone number or enter the details of your caravan with our free valuation form.</p>
    </article>

    <article class="abs step" style="left:252px">
      <div class="step-icon"><svg width="26" height="26" viewBox="0 0 26 26"><rect x="1" y="11" width="6" height="14" fill="#3b86c6"/><path d="M9 11 L14 2 C16 1 17.5 2.5 17 5 L16 10 H23 C25 10 25.5 12 24.5 13.5 C25.5 15 25 16.5 24 17 C24.8 18.5 24 20 23 20.5 C23.5 22 22.5 24.5 20.5 24.5 H9 Z" fill="#3b86c6"/></svg></div>
      <h3 class="thin-heading step-title">Accept our offer</h3>
      <p class="step-text">If you choose to accept our offer, we will soon be in touch to arrange the free collection of your caravan at a time convenient for you.</p>
    </article>

    <article class="abs step" style="left:467px">
      <div class="step-icon"><svg width="28" height="22" viewBox="0 0 28 22"><rect x="1" y="3" width="26" height="16" fill="none" stroke="#3b86c6" stroke-width="2.5"/><circle cx="14" cy="11" r="5" fill="#3b86c6"/><rect x="13" y="8" width="2" height="6" fill="#fff"/></svg></div>
      <h3 class="thin-heading step-title">Receive payment</h3>
      <p class="step-text">We can pay by cash if shown some photo ID, or alternatively, transfer the payment direct to your account.</p>
    </article>

    <div class="abs selling-note">Selling your Caravan?</div>
    <svg class="abs note-arrow" width="48" height="36" viewBox="0 0 48 36"><path d="M4 2 C2 18 16 30 42 28" fill="none" stroke="#333" stroke-width="2"/><path d="M35 21 L43 28 L35 34" fill="none" stroke="#333" stroke-width="2"/></svg>
    <div class="abs start-btn">
      <svg width="17" height="17" viewBox="0 0 17 17"><circle cx="8.5" cy="8.5" r="8.5" fill="#fff"/><path d="M6.5 4.5 L12.5 8.5 L6.5 12.5 Z" fill="#3b86c6"/></svg>
      <span>Get Started Now</span>
    </div>
  </section>

  <section class="collection">
    <div class="abs uk-map" role="img" aria-label="Map of the United Kingdom showing collection coverage"></div>
    <h2 class="abs thin-heading section-title collection-title">Free Collection</h2>
    <p class="abs collection-sub">Below are some examples of the areas we cover</p>
    <ul class="abs areas" style="left:177px"><li>Birmingham</li><li>Cambridge</li><li>Chelmsford</li><li>Chichester</li><li>Chester</li></ul>
    <ul class="abs areas" style="left:280px"><li>Exeter</li><li>Hertford</li><li>Leominster</li><li>Lincoln</li><li>Maidstone</li></ul>
    <ul class="abs areas" style="left:380px"><li>Manchester</li><li>Norwich</li><li>Swansea</li><li>Truro</li><li>Wakefield</li></ul>
  </section>

  <section class="testimonials">
    <h2 class="abs thin-heading section-title testimonials-title">Testimonials</h2>
    <blockquote class="abs quote">It was a pleasure &nbsp;to meet you Glen, thank you for a stress free sale of our caravan. I hope she goes to a good home.</blockquote>
    <svg class="abs quote-tail" width="16" height="12" viewBox="0 0 16 12"><path d="M0 0 H16 L10 12 Z" fill="#7aab1f"/></svg>
    <div class="abs quote-name">R. Hale</div>
    <div class="abs quote-model">- Ridgeway Tourer</div>
  </section>

  <div class="abs partner-band"></div>
  <div class="abs partner-grid" aria-label="Caravan makes we buy">
    <div class="partner"><span></span></div><div class="partner"><span></span></div><div class="partner"><span></span></div><div class="partner"><span></span></div><div class="partner"><span></span></div>
    <div class="partner"><span></span></div><div class="partner"><span></span></div><div class="partner"><span></span></div><div class="partner"><span></span></div><div class="partner"><span></span></div>
    <div class="partner"><span></span></div><div class="partner"><span></span></div><div class="partner"><span></span></div><div class="partner"><span></span></div><div class="partner"><span></span></div>
    <div class="partner"><span></span></div><div class="partner"><span></span></div><div class="partner"><span></span></div><div class="partner"><span></span></div><div class="partner"><span></span></div>
    <div class="partner"><span></span></div><div class="partner"><span></span></div><div class="partner"><span></span></div><div class="partner"><span></span></div><div class="partner"><span></span></div>
    <div class="partner"><span></span></div><div class="partner"><span></span></div><div class="partner"><span></span></div><div class="partner"><span></span></div><div class="partner"><span></span></div>
  </div>

  <footer>
    <div class="abs footer"></div>
    <ul class="abs footer-links"><li>Home</li><li>How it Works</li><li>FAQ's</li><li>Contact us</li></ul>
    <div class="abs footer-company">Trail Quote</div>
    <div class="abs footer-address">Orchard Lane, Millbrook, Essex CM00 1AB</div>
    <div class="abs footer-copy">Copyright 2014 Trailquote.example All Right Reserved.</div>
  </footer>

</div>
</body>
</html>
```